www.belvunit.com

Website design for IT outsourcing company (Belvun IT)
Pages: Home, About Us, Services, Case Studies, Careers, Contact and more (see current website for guidance)
Include client testimonials
Include client logos (e.g., Dulvane, etc)
List of services (staffing, app dev, integration, cloud)
Modern, clean, professional design
Blue/white/gray color scheme
Mobile and desktop responsive
Include call-to-action buttons
Space for case studies/project highlights

```html
<!DOCTYPE html>
<html lang="en">
<head>
<meta charset="utf-8">
<title>Case Studies – Belvun IT</title>
<link rel="stylesheet" href="https://fonts.googleapis.com/css2?family=Montserrat:wght@400;700&family=Roboto:wght@400;500;700&display=swap">
<style>
:root{
  --navy:#0d1b3e;
  --sky:#92c4dd;
  --sky-soft:#9ccbe0;
  --hero-bg:#dfe3e8;
  --text:#1b2233;
  --muted:#5b6270;
  --white:#ffffff;
  --line:#d8dde3;
}
*{margin:0;padding:0;box-sizing:border-box}
html,body{width:1200px;height:3027px;overflow:hidden}
body{position:relative;background:var(--white);font-family:"Roboto",sans-serif;color:var(--text)}
.abs{position:absolute}

/* header */
.hero{left:0;top:0;width:1200px;height:620px;background:linear-gradient(90deg,#e4e7eb 0%,#d9dee3 60%,#cfd5db 100%);overflow:hidden}
.hero-photo{left:560px;top:90px;width:640px;height:540px;background:radial-gradient(ellipse at 55% 45%,#aebfd0 0%,#c3cdd8 45%,#d9dee3 80%)}
.brand{left:112px;top:40px;display:flex;align-items:center;gap:8px;font-family:"Montserrat",sans-serif;font-weight:700;font-size:18px;letter-spacing:1px;color:var(--sky-soft)}
.brand-dot{width:14px;height:14px;border-radius:50%;background:var(--sky-soft)}
.nav{left:414px;top:60px;display:flex;gap:29px;font-size:15px;font-weight:500;color:var(--text)}
.nav .active{color:var(--sky-soft)}
.cta{left:952px;top:48px;width:137px;height:42px;background:var(--sky-soft);clip-path:polygon(14% 0,100% 0,100% 100%,0 100%);display:flex;align-items:center;justify-content:center;padding-left:14px;font-size:15px;font-weight:500;color:var(--navy)}
.hero-title{left:112px;top:244px;font-family:"Montserrat",sans-serif;font-size:45px;color:var(--navy);letter-spacing:1px}
.hero-title b{font-weight:700}
.hero-title span{font-weight:400}
.hero-edge{left:0;top:440px}

/* cases */
.case{width:311px;height:362px}
.case-media{left:0;top:0;width:311px;height:217px}
.case-card{left:0;top:164px;width:291px;height:198px;background:var(--white);box-shadow:0 6px 18px rgba(13,27,62,.08);padding:32px 29px 0}
.case-meta{font-size:13.5px;color:var(--navy);letter-spacing:.2px}
.case-title{margin-top:10px;font-size:18px;font-weight:700;line-height:26px;color:var(--text)}
.case-text{margin-top:14px;font-size:13.5px;line-height:23px;color:var(--muted)}

/* contact */
.contact-shape{left:0;top:1930px}
.contact-title{left:0;top:2088px;width:1200px;text-align:center;font-family:"Montserrat",sans-serif;font-size:40px;color:var(--navy)}
.contact-title b{font-weight:700}
.contact-rule{left:566px;top:2146px;width:68px;height:4px;background:var(--white)}
.field{background:var(--white);height:51px;padding:0 20px;display:flex;align-items:center;font-size:14px;color:#8a909a}
.field.msg{height:90px;align-items:flex-start;padding-top:18px}
.submit{left:508px;top:2477px;width:184px;height:52px;border-radius:26px;background:var(--navy);color:var(--white);display:flex;align-items:center;justify-content:center;font-size:15px;font-weight:700;letter-spacing:.5px}

/* footer */
.foot-brand{left:129px;top:2850px;width:160px;text-align:center;font-family:"Montserrat",sans-serif;font-weight:700;font-size:24px;letter-spacing:1px;color:var(--sky-soft)}
.foot-badge{left:189px;top:2760px;width:40px;height:40px;background:var(--sky-soft)}
.social{width:30px;height:30px;border:1px solid #c7ccd3;border-radius:50%;top:2897px;display:flex;align-items:center;justify-content:center;font-size:11px;font-weight:700;color:var(--text)}
.foot-col h4{font-size:17px;font-weight:700;color:var(--text);margin-bottom:18px}
.foot-col li{list-style:none;font-size:14px;color:var(--muted);height:27.5px}
.info{display:flex;gap:12px;margin-bottom:14px}
.info svg{flex:none;margin-top:2px}
.info strong{display:block;font-size:12px;color:var(--text);font-weight:700}
.info p{font-size:14px;color:var(--muted);line-height:19px}
.foot-rule{left:112px;top:2957px;width:976px;height:1px;background:var(--line)}
.copyright{left:0;top:2983px;width:1200px;text-align:center;font-size:15px;color:var(--muted)}
.to-top{left:1105px;top:2940px;width:36px;height:36px;border-radius:50%;background:var(--sky-soft);display:flex;align-items:center;justify-content:center}
</style>
</head>
<body>

<header class="abs hero">
  <div class="abs hero-photo" role="img" aria-label="Photo of a team of colleagues smiling around a laptop in a bright office"></div>
  <div class="abs brand"><span class="brand-dot"></span>BELVUNIT</div>
  <nav class="abs nav">
    <span>Home</span><span>About Us</span><span>Services</span><span class="active">Case Studies</span><span>Careers</span><span>Contact</span>
  </nav>
  <div class="abs cta">Let's Talk</div>
  <h1 class="abs hero-title"><b>CASE</b> <span>STUDIES</span></h1>
  <svg class="abs hero-edge" width="1200" height="180" viewBox="0 0 1200 180">
    <polygon points="0,125 180,24 1200,120 1200,180 0,180" fill="var(--sky-soft)"/>
    <polygon points="0,140 180,44 1200,172 1200,180 0,180" fill="var(--white)"/>
  </svg>
</header>

<main>
  <section class="cases">
    <article class="abs case" style="left:112px;top:669px"><div class="abs case-media" role="img" aria-label="Server room with glowing cloud symbol" style="background:linear-gradient(180deg,#0f2a3d,#113c55 60%,#0c2333)"></div><div class="abs case-card"><p class="case-meta">30 MAY 2024 &nbsp;/&nbsp; JOHN DOE</p><h3 class="case-title">Lorem ipsum dolor sit amet, consectetur elit,</h3><p class="case-text">Sed ut perspiciatis unde omnis iste natus error sit voluptatem</p></div></article>
    <article class="abs case" style="left:444px;top:669px"><div class="abs case-media" role="img" aria-label="Monitors showing program code" style="background:linear-gradient(135deg,#1d6f9a,#0c2f4a 60%,#081c2e)"></div><div class="abs case-card"><p class="case-meta">30 MAY 2024 &nbsp;/&nbsp; JOHN DOE</p><h3 class="case-title">Lorem ipsum dolor sit amet, consectetur elit,</h3><p class="case-text">Sed ut perspiciatis unde omnis iste natus error sit voluptatem</p></div></article>
    <article class="abs case" style="left:777px;top:669px"><div class="abs case-media" role="img" aria-label="Digital technology icons over a desk" style="background:linear-gradient(135deg,#3a4a5e,#1b2a3d 60%,#142033)"></div><div class="abs case-card"><p class="case-meta">30 MAY 2024 &nbsp;/&nbsp; JOHN DOE</p><h3 class="case-title">Lorem ipsum dolor sit amet, consectetur elit,</h3><p class="case-text">Sed ut perspiciatis unde omnis iste natus error sit voluptatem</p></div></article>

    <article class="abs case" style="left:112px;top:1082px"><div class="abs case-media" role="img" aria-label="Hands joining copper gears" style="background:linear-gradient(135deg,#e9d7cc,#c9a48e 50%,#6c7584)"></div><div class="abs case-card"><p class="case-meta">30 MAY 2024 &nbsp;/&nbsp; JOHN DOE</p><h3 class="case-title">Lorem ipsum dolor sit amet, consectetur elit,</h3><p class="case-text">Sed ut perspiciatis unde omnis iste natus error sit voluptatem</p></div></article>
    <article class="abs case" style="left:444px;top:1082px"><div class="abs case-media" role="img" aria-label="Glowing padlock on a circuit board" style="background:linear-gradient(135deg,#0e2238,#3a2a3a 50%,#0b1a2d)"></div><div class="abs case-card"><p class="case-meta">30 MAY 2024 &nbsp;/&nbsp; JOHN DOE</p><h3 class="case-title">Lorem ipsum dolor sit amet, consectetur elit,</h3><p class="case-text">Sed ut perspiciatis unde omnis iste natus error sit voluptatem</p></div></article>
    <article class="abs case" style="left:777px;top:1082px"><div class="abs case-media" role="img" aria-label="Two businessmen talking in an office" style="background:linear-gradient(135deg,#3b4650,#7d8a96 50%,#5a7ea8)"></div><div class="abs case-card"><p class="case-meta">30 MAY 2024 &nbsp;/&nbsp; JOHN DOE</p><h3 class="case-title">Lorem ipsum dolor sit amet, consectetur elit,</h3><p class="case-text">Sed ut perspiciatis unde omnis iste natus error sit voluptatem</p></div></article>

    <article class="abs case" style="left:112px;top:1496px"><div class="abs case-media" role="img" aria-label="Developers working at computers in a dim office" style="background:linear-gradient(135deg,#163a52,#2c5b78 50%,#0e2436)"></div><div class="abs case-card"><p class="case-meta">30 MAY 2024 &nbsp;/&nbsp; JOHN DOE</p><h3 class="case-title">Lorem ipsum dolor sit amet, consectetur elit,</h3><p class="case-text">Sed ut perspiciatis unde omnis iste natus error sit voluptatem</p></div></article>
    <article class="abs case" style="left:444px;top:1496px"><div class="abs case-media" role="img" aria-label="Two colleagues looking at a laptop" style="background:linear-gradient(135deg,#d7dadd,#9aa0a6 50%,#4c5058)"></div><div class="abs case-card"><p class="case-meta">30 MAY 2024 &nbsp;/&nbsp; JOHN DOE</p><h3 class="case-title">Lorem ipsum dolor sit amet, consectetur elit,</h3><p class="case-text">Sed ut perspiciatis unde omnis iste natus error sit voluptatem</p></div></article>
    <article class="abs case" style="left:777px;top:1496px"><div class="abs case-media" role="img" aria-label="Data center corridor with cloud symbol" style="background:linear-gradient(180deg,#0c2c5a,#1f5fa6 55%,#0a2248)"></div><div class="abs case-card"><p class="case-meta">30 MAY 2024 &nbsp;/&nbsp; JOHN DOE</p><h3 class="case-title">Lorem ipsum dolor sit amet, consectetur elit,</h3><p class="case-text">Sed ut perspiciatis unde omnis iste natus error sit voluptatem</p></div></article>
  </section>

  <section class="contact">
    <svg class="abs contact-shape" width="1200" height="800" viewBox="0 0 1200 800">
      <polygon points="0,9 1037,132 1200,38 1200,800 0,800" fill="var(--sky)"/>
      <polygon points="1037,132 1200,38 1200,66" fill="var(--navy)"/>
      <polygon points="0,752 180,642 1200,770 1200,800 0,800" fill="var(--navy)"/>
      <polygon points="0,770 180,668 1200,792 1200,800 0,800" fill="var(--white)"/>
    </svg>
    <h2 class="abs contact-title"><b>CONTACT</b> US</h2>
    <div class="abs contact-rule"></div>
    <div class="abs field" style="left:184px;top:2200px;width:408px">First Name *</div>
    <div class="abs field" style="left:606px;top:2200px;width:408px">Last Name *</div>
    <div class="abs field" style="left:184px;top:2267px;width:408px">Phone Number *</div>
    <div class="abs field" style="left:606px;top:2267px;width:408px">Email Address *</div>
    <div class="abs field msg" style="left:184px;top:2334px;width:830px">Message</div>
    <div class="abs submit">SUBMIT NOW</div>
  </section>
</main>

<footer>
  <div class="abs foot-badge"></div>
  <div class="abs foot-brand">BELVUNIT</div>
  <div class="abs social" style="left:153px">f</div>
  <div class="abs social" style="left:193px">X</div>
  <div class="abs social" style="left:232px">in</div>

  <div class="abs foot-col" style="left:387px;top:2740px"><h4>Quick Links</h4><ul><li>Home</li><li>About Us</li><li>Services</li><li>Case Studies</li><li>Careers</li><li>Contact</li></ul></div>
  <div class="abs foot-col" style="left:591px;top:2740px"><h4>About Company</h4><ul><li>Privacy Policy</li><li>Terms of Service</li><li>Site Map</li><li>Imprint</li><li>Terms And Conditions</li></ul></div>
  <div class="abs foot-col" style="left:828px;top:2740px;width:260px">
    <h4>Contact Us</h4>
    <div class="info"><svg width="12" height="12" viewBox="0 0 24 24"><path d="M6.6 10.8a15 15 0 0 0 6.6 6.6l2.2-2.2c.3-.3.7-.4 1-.2 1.1.4 2.3.6 3.6.6.6 0 1 .4 1 1V20c0 .6-.4 1-1 1A17 17 0 0 1 3 4c0-.6.4-1 1-1h3.5c.6 0 1 .4 1 1 0 1.3.2 2.5.6 3.6.1.3 0 .7-.2 1z" fill="var(--sky)"/></svg><div><strong>Opening Hours</strong><p>Mon - Fri 8:30 AM to 5:30 PM</p></div></div>
    <div class="info"><svg width="14" height="11" viewBox="0 0 24 18"><rect width="24" height="18" rx="2" fill="var(--sky)"/><path d="M1 2l11 8 11-8" stroke="#fff" stroke-width="2" fill="none"/></svg><div><strong>Email</strong><p>admin@belvunit.com</p></div></div>
    <div class="info"><svg width="12" height="14" viewBox="0 0 24 30"><path d="M12 0a11 11 0 0 0-11 11c0 8 11 19 11 19s11-11 11-19A11 11 0 0 0 12 0z" fill="var(--sky)"/><circle cx="12" cy="11" r="4" fill="#fff"/></svg><div><strong>Location</strong><p>Kelmora Road, Dravik Heights<br>(Ostra Bank Building)</p></div></div>
  </div>

  <div class="abs foot-rule"></div>
  <p class="abs copyright">2025 Copyright - &nbsp;Belvun IT. &nbsp;| All Rights Reserved</p>
  <div class="abs to-top"><svg width="14" height="10" viewBox="0 0 14 10"><path d="M1 8l6-6 6 6" stroke="#fff" stroke-width="2" fill="none"/></svg></div>
</footer>

</body>
</html>
```